Vegan Jerky company needs a label for it's pouch, and a new logo

Dear Designers - this used to be a guaranteed project, however, due to the low quality of designs I have received, I have removed the guaranteed status. However, we need this product made and we will pay for a great, high quality design that meets the requirements of our brief.

We need sticker labels that will go onto the front and back of our vegan jerky package. Our package is a zip-sealable pouch, and we will either go with black, white or brown for the color of the pouch.

We need the concept, artwork, theme and logo designed. Pls choose the colors.

There will be four flavors. These can be finished as part of another project. The flavors are: Smoked Maple, Cracked Pepper, Teriyaki Sriracha, Original.

We are Lonny and Marva's Vegan Jerky.

Our food is vegan, non GMO, straight from the farm, organic, healthy, pure, clean, made in small batches and earth friendly. We use no chemicals or artificial flavors and our product is 100% natural.

Our kitchen is yours.
Updates

Low designer entries

Target Market(s)

Vegetarians, vegans, health conscious, ecological, intelligent, caring.

Industry/Entity Type

Food Production

Logo Text

"Lonny and Marva" and "Our Kitchen is Yours"

Colors

Designer to choose colors to be used in the design.

Requirements
Must have
• earth friendly design, classy, hipster, vegan design, shabby chic,
Nice to have
• i have no ideas really...
• We prefer black and while, with a little splash of color. The last file is an idea I had but please use your own vision.

```html
<!DOCTYPE html>
<html lang="en">
<head>
<meta charset="utf-8">
<title>Lonny and Marva's Vegan Jerky – Smoked Maple Label</title>
<link href="https://fonts.googleapis.com/css2?family=Courier+Prime:wght@700&family=Josefin+Sans:wght@700&display=swap" rel="stylesheet">
<style>
  :root {
    --page: #ffffff;
    --kraft: #cdb388;
    --kraft-light: #d8c198;
    --kraft-dark: #b89a6c;
    --ink: #2e1f14;
    --logo-brown: #6a5240;
    --banner-green: #4f9a48;
    --leaf-rust: #a65a3a;
    --leaf-olive: #a7a05a;
    --leaf-sage: #b9b27c;
    --jerky-dark: #6b3418;
    --jerky-mid: #a8622c;
    --jerky-light: #d39a55;
  }
  * { margin: 0; padding: 0; box-sizing: border-box; }
  html, body {
    width: 1200px; height: 1200px; overflow: hidden;
    background: var(--page);
  }
  .label {
    position: absolute;
    left: 225px; top: 47px;
    width: 750px; height: 1105px;
    background:
      radial-gradient(ellipse at 30% 20%, var(--kraft-light) 0%, transparent 60%),
      radial-gradient(ellipse at 80% 85%, var(--kraft-dark) 0%, transparent 55%),
      var(--kraft);
    overflow: hidden;
  }
  .leaf-art {
    position: absolute;
    border-radius: 50%;
    filter: blur(2px);
  }
  .leaf-art--top-left {
    left: -40px; top: 20px; width: 200px; height: 120px;
    background: radial-gradient(ellipse, rgba(150,140,90,0.35), transparent 70%);
    transform: rotate(25deg);
  }
  .leaf-art--right {
    right: -20px; top: 480px; width: 130px; height: 300px;
    background: radial-gradient(ellipse, rgba(150,150,100,0.45), transparent 70%);
    transform: rotate(20deg);
  }
  .leaf-art--bottom-left {
    left: 0; top: 790px; width: 320px; height: 310px;
    background:
      radial-gradient(ellipse at 30% 45%, rgba(166,90,58,0.55), transparent 50%),
      radial-gradient(ellipse at 65% 60%, rgba(167,160,90,0.5), transparent 55%);
  }
  .leaf-art--bottom-right {
    right: 20px; top: 880px; width: 230px; height: 150px;
    background: radial-gradient(ellipse, rgba(185,178,124,0.55), transparent 70%);
    transform: rotate(-15deg);
  }
  .brand-name {
    position: absolute;
    left: 0; right: 0; top: 178px;
    text-align: center;
    font-family: "Josefin Sans", sans-serif;
    font-weight: 700;
    font-size: 74px;
    line-height: 1;
    letter-spacing: -1px;
    color: var(--logo-brown);
  }
  .banner {
    position: absolute;
    left: 88px; top: 318px;
    width: 590px; height: 70px;
  }
  .banner__shape {
    fill: none;
    stroke: var(--banner-green);
    stroke-width: 5;
    stroke-linejoin: round;
  }
  .banner__text {
    position: absolute;
    inset: 0;
    display: flex; align-items: center; justify-content: center;
    padding-top: 6px;
    font-family: "Josefin Sans", sans-serif;
    font-weight: 700;
    font-size: 44px;
    letter-spacing: 5px;
    color: var(--banner-green);
  }
  .claim {
    position: absolute;
    left: 80px; top: 447px;
    font-family: "Josefin Sans", sans-serif;
    font-weight: 700;
    font-size: 30px;
    letter-spacing: 3.5px;
    color: var(--ink);
  }
  .flavour {
    position: absolute;
    left: 80px; top: 488px;
    font-family: "Courier Prime", monospace;
    font-weight: 700;
    font-size: 88px;
    line-height: 1.1;
    letter-spacing: -3px;
    color: var(--ink);
    transform: scaleY(1.3);
    transform-origin: left top;
  }
  .window {
    position: absolute;
    left: 84px; top: 627px;
    width: 581px; height: 228px;
    border-radius: 10px;
    background:
      radial-gradient(ellipse at 30% 40%, var(--jerky-light), transparent 55%),
      radial-gradient(ellipse at 75% 70%, var(--jerky-mid), transparent 60%),
      linear-gradient(180deg, var(--jerky-mid), var(--jerky-dark));
  }
</style>
</head>
<body>
  <main class="label">
    <div class="leaf-art leaf-art--top-left" role="img" aria-label="Faint hand-drawn leaf illustration"></div>
    <div class="leaf-art leaf-art--right" role="img" aria-label="Faint hand-drawn leaf illustration"></div>

    <header>
      <div class="brand-name">Lonny and Marva's</div>
      <div class="banner">
        <svg class="banner__svg" width="590" height="70" viewBox="0 0 590 70" aria-hidden="true">
          <polygon class="banner__shape" points="4,6 586,6 562,35 586,64 4,64 28,35"/>
        </svg>
        <div class="banner__text">VEGAN JERKY</div>
      </div>
    </header>

    <p class="claim">100% NATURAL</p>
    <h1 class="flavour">Smoked Maple</h1>

    <div class="window" role="img" aria-label="Clear window showing smoked maple vegan jerky pieces"></div>

    <div class="leaf-art leaf-art--bottom-left" role="img" aria-label="Hand-drawn rust and olive leaf illustrations"></div>
    <div class="leaf-art leaf-art--bottom-right" role="img" aria-label="Hand-drawn pale leaf illustration"></div>
  </main>
</body>
</html>
```